依頼詳細
店舗かんばんのデザインをお願いしたく思います。ただし、仕様がタペストリーとなります。(壁に貼り付ける感じです)
重視したい事は、第一目立つこと。文字のなかではお葬式相談室の文字を一番目立たしたいです。店内の雰囲気はちょっとしたカフェのような感じなので、入りやすいような、やわらかいイメージのデザインが好ましいです。また、お葬式自体暗いイメージなので明るい印象もつけたいです。
記載項目
お葬式相談室/桐野葬祭/電話番号/ルミナード楓/いろんなありがとうがあるお葬式を・・・。
参考:http://www.kanade-hall.co.jp/
希望イメージ
シンプル 複雑
単色 カラフル
暗い 明るい
日常 高級
遊び心 厳粛
未来的 伝統的
女性的 男性的
希望する色
納品ファイル
• 高解像度JPG (.jpg)
• イラストレーター形式 (.ai)
補足説明
納品ファイルは、後日ご連絡致します。また、会社のロゴデータも後日添付致します
サイズ:W1800 H2800となります。
皆様。お世話になります。
たくさんのご提案ありがとうございます。

追記内容についてですが、2点ございます。
①「お葬式相談室」の上部、キャッチの部分に「お葬式のご相談・お悩みが解決できる」と記載して頂きたいと思います。
②「お葬式相談室」下記部分には「仏壇・ろうそく・線香も取り扱っております」と記載して頂きたいと思います。
※ただ、こちらについて仏壇を取り扱うかどうか、まだ確定していない事もあり、場合によっては、「仏壇」の部分を「仏花」に変えて頂く場合もございます。

今回、修正がございましたので、締切期間を延期させて頂きます。

みなさまには、ご迷惑をおかけいたしますが、
何卒、よろしくお願い申し上げます。
皆様。お世話になります。下記追記内容を記載します。

①弊社では、コーポレートカラーを青としており、他の店舗看板など販促物も青と白を基調にしている事が多いので、今回も同じように合わす事ができればと思います。

②ロゴはコスモスを表しております。
背景にコスモスの花を入れて頂いたりするデザインがあれば一度拝見してみたいと考えております。また、ご家族の写真を記載したデザインも安心感が訴求されるので、
一度見てみたいと思います。

③道を挟んだ場所に区役所がございます。看板を見られるメインの対象者となります。なので、その距離感を踏まえ、文字等の大きさの調整を行って頂ければと思います。下記は、看板の構成を記載しております。

【フック(左上)どんなお店か】「お葬式の相談・お悩み事が解決できる」⇒【タイトル】「お葬式相談室」⇒【なにを扱っているか】「仏壇・ろうそく・線香(大きく)」取り扱っております。⇒【どの会社が】「いろんなありがとうがあるお葬式を・・・桐野葬祭」(ルミナード楓より桐野葬祭の方が大きめでお願いします。)
⇒【問い合わせ】TEL(24時間~)

参考までに、現在の店舗写真を添付致します。撮影場所は上記でご説明させて頂いた、区役所前からの写真となります。

何卒、宜しくお願い致します。
看板設置イメージを添付致します。

P.S
一度会議で、デザインを相談したいと考えているためできれば30日までにご連絡いただけると幸いです。

宜しくお願い致します。
■ 選んだ理由

お世話になります。今回、この提案を選んだ理由は、こちらの希望に沿い、弊社の”らしさ”を忠実の表現して頂いたからです。
また、目立たせるポイントの色使いなども気に入りました。

■ 提案者全員のお礼・コメント

今回、提案していただいたみなさまへ。
はじめての利用という事もあり、みなさまへのご配慮が足りない部分もありましたが、たくさんのご提案ありがとうございました。

また、機会があればどうぞ宜しくお願い致します。

```html
<!DOCTYPE html>
<html lang="ja">
<head>
<meta charset="utf-8">
<title>お葬式相談室 タペストリー</title>
<link rel="stylesheet" href="https://fonts.googleapis.com/css2?family=Kaisei+Decol:wght@700&family=M+PLUS+Rounded+1c:wght@500;700;800&display=swap">
<style>
  :root {
    --sky: #d5e5f5;
    --blush: #f8e4eb;
    --cream: #fbf1f0;
    --leaf: #e3efc4;
    --pink: #eb9fae;
    --pink-deep: #e0708a;
    --white: #ffffff;
    --ink: #5a5a5a;
    --blue: #2f64a8;
    --blue-soft: #4f82ba;
    --green: #6aaf4a;
    --flower: #d9434a;
    --flower-soft: #ec8a86;
  }
  * { margin: 0; padding: 0; box-sizing: border-box; }
  html, body { width: 770px; height: 1200px; overflow: hidden; }
  body {
    position: relative;
    font-family: "M PLUS Rounded 1c", sans-serif;
    background: linear-gradient(180deg, var(--sky) 0%, var(--blush) 32%, var(--cream) 62%, var(--leaf) 100%);
    color: var(--ink);
  }
  .catch {
    position: absolute; top: 26px; left: 0; width: 100%;
    text-align: center; font-size: 28px; font-weight: 700; letter-spacing: 1px;
  }
  .catch em { font-style: normal; color: var(--pink-deep); }

  .title-panel {
    position: absolute; left: 77px; top: 90px; width: 616px; height: 660px;
    background: var(--pink); border-radius: 40px;
  }
  .title-panel::after {
    content: ""; position: absolute; inset: 18px;
    border: 5px solid var(--white); border-radius: 28px;
  }
  .title-char {
    position: absolute; color: var(--white);
    font-family: "Kaisei Decol", serif; font-weight: 700; line-height: 1;
  }
  .title-o { left: 40px; top: 40px; font-size: 310px; }
  .title-soushiki {
    left: 368px; top: 52px; font-size: 150px;
    writing-mode: vertical-rl; letter-spacing: 6px;
  }
  .title-soudanshitsu { left: 36px; top: 430px; font-size: 178px; letter-spacing: 4px; }

  .flower-art {
    position: absolute; left: 18px; top: 690px; width: 120px; height: 110px;
    border-radius: 18px;
    background: linear-gradient(160deg, var(--flower) 0%, var(--flower-soft) 100%);
  }

  .lead {
    position: absolute; top: 796px; left: 0; width: 100%;
    text-align: center; font-size: 18px; line-height: 1.7; font-weight: 500;
  }

  .phone {
    position: absolute; top: 940px; left: 170px;
    display: flex; align-items: center; gap: 14px;
    color: var(--blue-soft);
  }
  .phone svg { width: 60px; height: 52px; }
  .phone-number { font-size: 70px; font-weight: 700; letter-spacing: 1px; line-height: 1; }

  .notes {
    position: absolute; top: 1036px; left: 110px;
    font-size: 13px; line-height: 1.55; color: var(--green); font-weight: 700;
  }

  .branch {
    position: absolute; top: 1036px; left: 372px;
    display: flex; align-items: center; gap: 10px;
    color: var(--blue); font-size: 34px; font-weight: 700; line-height: 1.2;
  }
  .brand-dot { width: 22px; height: 22px; border-radius: 50%; background: var(--blue); flex: none; }

  .company {
    position: absolute; top: 1104px; left: 140px;
    display: flex; align-items: center; gap: 14px;
  }
  .company .brand-dot { width: 44px; height: 44px; }
  .company-name { color: var(--blue); font-size: 64px; font-weight: 800; letter-spacing: 2px; line-height: 1; }
  .since {
    margin-left: 12px; height: 74px; padding: 0 10px;
    background: var(--blue); color: var(--white); border-radius: 4px;
    display: flex; align-items: center; gap: 6px; font-weight: 700;
  }
  .since-small { writing-mode: vertical-rl; font-size: 18px; line-height: 1; height: 40px; text-align: center; }
  .since-num { font-size: 52px; line-height: 1; }
</style>
</head>
<body>
  <p class="catch">いろんな<em>「ありがとう」</em>があるお葬式を…</p>

  <div class="title-panel">
    <span class="title-char title-o">お</span>
    <span class="title-char title-soushiki">葬式</span>
    <span class="title-char title-soudanshitsu">相談室</span>
  </div>

  <div class="flower-art" role="img" aria-label="赤いコスモスの花のイラスト"></div>

  <p class="lead">大阪市で家族葬のことなら桐野葬祭へ。<br>いろんなありがとうがあるお葬式を安心料金でご提供させて頂きます。</p>

  <div class="phone">
    <svg viewBox="0 0 56 48" aria-hidden="true">
      <path d="M6 16 C6 8 14 4 28 4 C42 4 50 8 50 16 L50 20 L40 20 L38 13 C32 11 24 11 18 13 L16 20 L6 20 Z" fill="none" stroke="currentColor" stroke-width="4" stroke-linejoin="round"/>
      <path d="M14 24 L42 24 L48 44 L8 44 Z" fill="none" stroke="currentColor" stroke-width="4" stroke-linejoin="round"/>
      <circle cx="28" cy="34" r="5" fill="currentColor"/>
    </svg>
    <span class="phone-number">0120-456-789</span>
  </div>

  <p class="notes">24時間受付 年中無休<br>事前相談 お見積無料<br>家族葬 一般葬 対応</p>

  <div class="branch"><span class="brand-dot"></span><span>ルミナード楓</span></div>

  <div class="company">
    <span class="brand-dot"></span>
    <span class="company-name">桐野葬祭</span>
    <span class="since"><span class="since-small">創業</span><span class="since-num">70</span><span class="since-small">余年</span></span>
  </div>
</body>
</html>
```